Business Card

I would like a business card with a picture of my husband and I that is unique and professional.

Industry/Entity Type

Business

Font styles to use
Serif

```html
<!DOCTYPE html>
<html lang="en">
<head>
<meta charset="utf-8">
<title>Whitfield Leadership Group – Business Card</title>
<link rel="stylesheet" href="https://fonts.googleapis.com/css2?family=Questrial&display=swap">
<style>
  :root {
    --backdrop: #ece9e4;
    --card: #ffffff;
    --gold: #f0a93a;
    --gold-deep: #d18d22;
    --ink: #1c1c1c;
    --charcoal: #3a3b3e;
    --band: #6d6f73;
    --photo-light: #d9d6d2;
    --photo-mid: #8a7f78;
    --photo-dark: #4b403b;
  }
  * { box-sizing: border-box; margin: 0; padding: 0; }
  html, body {
    width: 1200px; height: 784px; overflow: hidden;
    background: var(--backdrop);
    font-family: "Questrial", "Century Gothic", sans-serif;
    color: var(--ink);
  }
  .stage {
    position: relative; width: 1200px; height: 784px;
    display: flex; align-items: center; justify-content: center; gap: 40px;
  }
  .card {
    position: relative; width: 540px; height: 309px;
    background: var(--card); overflow: hidden;
    box-shadow: 0 8px 24px rgba(0,0,0,.18);
  }

  /* Front */
  .card--front { display: flex; align-items: center; justify-content: center; }
  .brand { display: flex; align-items: center; gap: 12px; }
  .brand__dot {
    width: 22px; height: 22px; border-radius: 50%; background: var(--gold);
  }
  .brand__name { font-size: 26px; color: var(--charcoal); letter-spacing: .5px; }

  /* Back */
  .card--back .brand { position: absolute; left: 40px; top: 58px; gap: 8px; }
  .card--back .brand__dot { width: 14px; height: 14px; }
  .card--back .brand__name { font-size: 16px; }
  .brand-rule {
    position: absolute; left: 40px; top: 92px; width: 190px; height: 1px;
    background: var(--charcoal);
  }
  .portrait {
    position: absolute; right: 0; top: 0; width: 205px; height: 226px;
    background: radial-gradient(ellipse at 55% 60%, var(--photo-mid), var(--photo-dark) 55%, var(--photo-light) 100%);
  }
  .identity { position: absolute; left: 40px; top: 128px; }
  .identity__name { font-size: 20px; color: var(--gold); line-height: 1.2; }
  .identity__title { font-size: 13px; color: var(--ink); margin-top: 2px; }
  .contact { position: absolute; left: 40px; top: 196px; list-style: none; }
  .contact__item {
    display: flex; align-items: center; gap: 10px;
    font-size: 15px; line-height: 22px;
  }
  .contact__icon { width: 14px; height: 14px; fill: var(--gold); }
  .footer-band { position: absolute; left: 0; bottom: 0; width: 540px; height: 80px; }
</style>
</head>
<body>
<main class="stage">
  <section class="card card--front" aria-label="Card front">
    <div class="brand">
      <span class="brand__dot"></span>
      <span class="brand__name">Whitfield Leadership Group</span>
    </div>
  </section>

  <section class="card card--back" aria-label="Card back">
    <div class="brand">
      <span class="brand__dot"></span>
      <span class="brand__name">Whitfield Leadership Group</span>
    </div>
    <div class="brand-rule"></div>

    <div class="portrait" role="img" aria-label="Portrait photo of the couple, smiling, in grey suits"></div>

    <div class="identity">
      <p class="identity__name">Dana Whitfield</p>
      <p class="identity__title">Professional Mentorship Strategist</p>
    </div>

    <ul class="contact">
      <li class="contact__item">
        <svg class="contact__icon" viewBox="0 0 24 24" aria-hidden="true"><path d="M6.6 10.8a15.1 15.1 0 0 0 6.6 6.6l2.2-2.2c.3-.3.7-.4 1-.2 1.1.4 2.3.6 3.6.6.6 0 1 .4 1 1V20c0 .6-.4 1-1 1A17 17 0 0 1 3 4c0-.6.4-1 1-1h3.5c.6 0 1 .4 1 1 0 1.3.2 2.5.6 3.6.1.3 0 .7-.2 1z"/></svg>
        <span>312-555-0148</span>
      </li>
      <li class="contact__item">
        <svg class="contact__icon" viewBox="0 0 24 24" aria-hidden="true"><path d="M2 5h20v14H2z M3.5 6.5 12 13l8.5-6.5" fill="none" stroke="currentColor"/><path d="M2 5h20v14H2V5zm2 2v.3l8 5.6 8-5.6V7H4z"/></svg>
        <span>DanaWhitfield@mail.com</span>
      </li>
    </ul>

    <svg class="footer-band" viewBox="0 0 540 80" aria-hidden="true">
      <polygon points="0,72 540,14 540,80 0,80" fill="var(--band)"/>
      <polygon points="0,66 540,8 540,14 0,72" fill="var(--gold)"/>
      <polygon points="0,74 540,16 540,18 0,76" fill="#ffffff"/>
    </svg>
  </section>
</main>
</body>
</html>
```